Velora Crest Expo - a fashion, art, design exhibition

Please see below. The poster must be very elegant. Eventhough it has an african name and feel, it should be modern and elegant so that it attracts all types of backgrounds and races to the show.

I want this poster to be so good that it attracts Sponsors, partners and exhibitors to want to be part of the show. So its my key marketing document.

Size: A0. Good luck and be creative!

Brief is below

The VELORA CREST EXPO 2014

Dates: 19- 21 SEPTEMBER 2014:
all weekend event -open to the public
Time:
9am-5PM
OPEN TO THE PUBLIC
*Fashion shows will have exclusive show times

Venue to be confirmed

SHOWCASING
Fashion designers;
• Shoes designers;
• Accessory designers;
• Art;
• Cosmetics;
• Hair;
• Home and Décor;
• Media;
• Textiles and manufacturing;
• Technology;
• Tourism;
• Luxury/Lifestyle;
• Food & Others.

Countries representing:
SouthAfrica
Nigeria
Ghana
Kenya
Zimbabwe
Tanzania
Uganda
Ethiopia
Botswana
Mozambique
Zambia

To exhibit, partner or sponsor contact us:
Email: info@veloracrestexpo.com
Tele: 073 564 2187
Web: www.theveloracrestexpo.com
Facebook:/theveloracrestexpo
Twitter:@the veloracrestexpo

All rights reserved. Presented by Drembel International

Reason: I have extended the deadline because, one designer asked for it.

Please see the updated brief. I had alot of queries on the brief so i have shortened it.

Hi Designers,

I've attached our logo below. Please use logo version 2.1.3

We are interested in receiving more designs (right now there are only 2 to choose from)
Looking forward to your creativity.

Best regards

Hi all, Thanks for the designs that have been submitted. What i am really looking for is something that is elegant and catchy. The event/expo is an exhibition that will showcase, fashion, art, design, interior, comestics an hair etc. there will also be fashion shows that will be held on that day. It will be a nice classy event, that will draw crowds from all over Africa to participate. I have pasted the link below as a guide. Feel free to amend the brief or just use some of the info that will work. I need more designs. https://www.sample-lookup.example/search?q=example+poster+reference

Target Market(s)

The public/ in SouthA frica, Africa and the world:
-Fashion bloggers
-Magazine Editors
-Fashion Brands
-Industry experts

those who attend will want to see:

- To interact and socialise with entrepreneurs
- See what’s new
- Evaluate products and suppliers
- Keep abreast of industry and market developments
- Network/develop business contacts
Solve specific problems
- Find new markets
- Appoint agents/seek principals
- Discuss specific terms/conditions/pricing
- Consolidate business relationships

It will be an all weekend event. Adults aged 25 as per above

Industry/Entity Type

Marketing

Font styles to use
Serif

Requirements
Must have
• The poster must be elegant and appealing
Nice to have
• Be creative, think, Harbourline Style Days or Corvena style days and exhibition/trade fair combined.

The event will be fashion driven, so that lifestyle brands can also exhibit there
Should not have
• No old style

Not tacky

Must be classy

```html
<!DOCTYPE html>
<html lang="en">
<head>
<meta charset="utf-8">
<title>The Velora Crest Expo 2014</title>
<link rel="stylesheet" href="https://fonts.googleapis.com/css2?family=Ubuntu:wght@300;400&display=swap">
<style>
  :root {
    --bg: #0a0a0a;
    --white: #ffffff;
    --text-soft: #b4b4b4;
    --text-muted: #9a9a9a;
    --text-country: #d0d0d0;
    --rule-light: #8a8a8a;
    --bar-light: #5c5c5c;
    --bar-dark: #2a2a2a;
    --mark: #c8206a;
    --ornament: #262626;
  }
  html, body { margin: 0; padding: 0; overflow: hidden; background: var(--bg); }
  .poster {
    position: relative; width: 1200px; height: 900px; overflow: hidden;
    background: var(--bg); font-family: "Ubuntu", sans-serif; font-weight: 300; color: var(--white);
  }
  .rule { position: absolute; left: 55px; width: 1105px; height: 5px;
    background: linear-gradient(90deg, transparent, var(--rule-light) 20%, var(--rule-light) 80%, transparent); }
  .rule--top { top: 32px; }
  .rule--bottom { top: 845px; }
  .ornament { position: absolute; left: 300px; top: 90px; width: 420px; height: 720px;
    background: radial-gradient(ellipse at center, var(--ornament), transparent 70%); opacity: .8; }
  .label-bar { position: absolute; height: 38px; display: flex; align-items: center; font-size: 20px; font-weight: 400; margin: 0; }
  .label-bar--left { left: 45px; padding-left: 10px; box-sizing: border-box;
    background: linear-gradient(90deg, var(--bar-dark) 0%, var(--bar-dark) 60%, var(--bar-light) 85%, transparent 100%); }
  .label-bar--right { right: 40px; justify-content: flex-end; padding-right: 7px; box-sizing: border-box;
    background: linear-gradient(270deg, var(--bar-dark) 0%, var(--bar-dark) 60%, var(--bar-light) 85%, transparent 100%); }
  .subline { position: absolute; left: 55px; top: 128px; margin: 0; font-size: 25px; color: var(--text-soft); }
  .showcase-list, .country-list, .contact-list { position: absolute; margin: 0; padding: 0; list-style: none; }
  .showcase-list { left: 60px; top: 450px; font-size: 18px; line-height: 28.7px; color: var(--text-muted); font-weight: 400; }
  .country-list { right: 47px; top: 135px; text-align: right; font-size: 22px; line-height: 41px; color: var(--text-country); }
  .contact-list { right: 47px; top: 688px; text-align: right; font-size: 20px; line-height: 29px; color: var(--text-soft); }
  .brand { position: absolute; left: 300px; top: 0; width: 412px; height: 900px; margin: 0;
    color: var(--white); font-weight: 300; line-height: 1; text-align: right; }
  .brand__line { position: absolute; right: 0; white-space: nowrap; }
  .brand__line--first { top: 334px; font-size: 56px; }
  .brand__line--second { top: 405px; font-size: 56px; }
  .brand__year { position: absolute; right: 12px; top: 470px; font-size: 72px; }
  .brand-mark { position: absolute; left: 740px; top: 195px; width: 250px; height: 250px;
    border-radius: 50%; background: var(--mark); }
  .footer { position: absolute; top: 864px; margin: 0; font-size: 14px; color: var(--text-muted); }
  .footer--left { left: 47px; }
  .footer--right { right: 40px; }
</style>
</head>
<body>
<main class="poster">
  <div class="rule rule--top"></div>
  <div class="ornament" role="img" aria-label="Faint flowing floral swirl ornament"></div>

  <p class="label-bar label-bar--left" style="top:79px;width:350px;">Dates: 19- 21 September 2014</p>
  <p class="subline">All weekend event -open to the public</p>
  <p class="label-bar label-bar--left" style="top:204px;width:250px;">Time : 9am - 5pm</p>
  <p class="label-bar label-bar--left" style="top:306px;width:250px;">Venue :</p>
  <p class="label-bar label-bar--left" style="top:395px;width:250px;padding-left:17px;">SHOWCASING</p>

  <ul class="showcase-list">
    <li>Fashion designers</li><li>Shoes designers</li><li>Accessory designers</li><li>Art</li>
    <li>Cosmetics</li><li>Hair</li><li>Home and Décor</li><li>Media</li>
    <li>Textiles and manufacturing</li><li>Technology</li><li>Tourism</li>
    <li>Luxury/Lifestyle</li><li>Food &amp; Others.</li>
  </ul>

  <div class="brand-mark" role="img" aria-label="Velora Crest Expo brand mark"></div>
  <h1 class="brand">
    <span class="brand__line brand__line--first">The VELORA</span>
    <span class="brand__line brand__line--second">CREST EXPO</span>
    <span class="brand__year">2014</span>
  </h1>

  <p class="label-bar label-bar--right" style="top:79px;width:435px;">Countries representing:</p>
  <ul class="country-list">
    <li>SouthAfrica</li><li>Nigeria</li><li>Ghana</li><li>Kenya</li><li>Zimbabwe</li>
    <li>Tanzania</li><li>Uganda</li><li>Ethiopia</li><li>Botswana</li><li>Mozambique</li><li>Zambia</li>
  </ul>

  <p class="label-bar label-bar--right" style="top:633px;width:440px;">To exhibit, partner or sponsor contact us:</p>
  <ul class="contact-list">
    <li>Email: info@veloracrestexpo.com</li>
    <li>Tele: 073 564 2187</li>
    <li>Web: www.theveloracrestexpo.com</li>
    <li>Facebook:/theveloracrestexpo</li>
    <li>Twitter:@the veloracrestexpo</li>
  </ul>

  <div class="rule rule--bottom"></div>
  <p class="footer footer--left">All rights reserved. Presented by Drembel International:</p>
  <p class="footer footer--right">*Fashion shows will have exclusive show times</p>
</main>
</body>
</html>
```